Business Card Design for Event Planning Company

Create a business card for event planning company using our new logo. After I pick the design, I will need files made for 6 employees. Our company provides event design & logistics services as well as venue management. The font should be sans serif and complementary to the logo. I will need to know the name of the font selected for the final design. The phone numbers listed should be separated by "." not "-"

Address for the card
PO Box 318, Washington, DC 20019

Card One
Lorna Pettibone
lpettibone@galavoyant.com
202.481.7730

Card Two
Miriam Okonkwo
mokonkwo@galavoyant.com
202.556.2047

Card Three
Tessa Varnholt
tvarnholt@galavoyant.com
978.620.4471

Card Four
Robin Fess
rfess@galavoyant.com
202.718.3362

Card Five
Ada-Rose Pelletan-Uzor
adarose@galavoyant.com
202.839.1205

Card Six
Beatrix Holloway
Beatrix@galavoyant.com
202.492.6618

Target Market(s)

Corporate/Non-Profit

Industry/Entity Type

Event Planning

Contact Information for Business Card

Address for the card

Card One
Lorna Pettibone
lpettibone@galavoyant.com
202.481.7730

Card Two
Miriam Okonkwo
202.556.2047

Card Three
Tessa Varnholt
978.620.4471

Card Four
Robin Fess
rfess@galavoyant.com
202.718.3362

Card Five
Ada-Rose Pelletan-Uzor
202.839.1205

Card Six
Beatrix Holloway
202.492.6618

Font styles to use
Sans Serif

Colors

Designer to choose colors to be used in the design.

Requirements
Must have
• Two-sided with logo
Should not have
• Extra colors or be too busy

```html
<!DOCTYPE html>
<html lang="en">
<head>
<meta charset="utf-8">
<title>Galavoyant Business Card</title>
<link rel="stylesheet" href="https://fonts.googleapis.com/css2?family=Jost:wght@400;500&display=swap">
<style>
  :root {
    --backdrop: #e8e5e1;
    --card-white: #f3f3f2;
    --card-black: #231f20;
    --teal: #5ba5a5;
    --ink: #3d3a3b;
    --rule: #8a8788;
  }
  * { margin: 0; padding: 0; box-sizing: border-box; }
  html, body { width: 1200px; height: 960px; overflow: hidden; }
  body {
    background: var(--backdrop);
    font-family: "Jost", "Futura", sans-serif;
    position: relative;
  }
  .card {
    position: absolute;
    width: 600px;
    height: 342px;
    border-radius: 18px;
    overflow: hidden;
    box-shadow: 0 3px 8px rgba(0,0,0,0.25);
  }
  .card-front { left: 302px; top: 130px; background: var(--card-white); }
  .card-back { left: 300px; top: 490px; background: var(--card-black); }
  .front-sweep { position: absolute; inset: 0; }

  .brand {
    position: absolute;
    display: flex;
    align-items: center;
    gap: 12px;
    color: var(--teal);
    font-weight: 400;
    letter-spacing: 0.5px;
    line-height: 1;
  }
  .brand-dot { border-radius: 50%; background: var(--teal); flex: none; }
  .card-front .brand { left: 44px; top: 112px; font-size: 40px; }
  .card-front .brand-dot { width: 22px; height: 22px; }
  .card-back .brand {
    left: 0; right: 0; top: 128px; justify-content: center; font-size: 46px;
  }
  .card-back .brand-dot { width: 26px; height: 26px; }

  .person-name {
    position: absolute;
    left: 44px; top: 172px;
    font-size: 22px;
    font-weight: 500;
    color: var(--teal);
    text-transform: uppercase;
    letter-spacing: 0.3px;
  }
  .contact-list {
    position: absolute;
    left: 46px; top: 219px;
    list-style: none;
    font-size: 14.5px;
    color: var(--ink);
  }
  .contact-list li { display: flex; align-items: center; gap: 9px; height: 20px; }
  .contact-list svg { width: 12px; height: 12px; fill: var(--teal); flex: none; }
  .divider {
    position: absolute;
    left: 256px; top: 222px;
    width: 1px; height: 54px;
    background: var(--rule);
  }
  .address {
    position: absolute;
    left: 279px; top: 221px;
    font-size: 14.5px;
    line-height: 20px;
    color: var(--ink);
    font-style: normal;
  }
</style>
</head>
<body>
  <section class="card card-front">
    <svg class="front-sweep" viewBox="0 0 600 342" aria-hidden="true">
      <rect width="600" height="342" fill="var(--teal)"/>
      <path d="M0 0 H473 C530 50 566 130 556 190 C 546 250 510 310 475 342 H0 Z" fill="var(--card-black)"/>
      <path d="M0 0 H473 C530 50 562 130 553 186 C 535 256 450 318 372 342 H0 Z" fill="var(--card-white)"/>
    </svg>

    <div class="brand"><span class="brand-dot"></span>galavoyant</div>
    <h1 class="person-name">Lorna Pettibone</h1>

    <ul class="contact-list">
      <li>
        <svg viewBox="0 0 12 12"><path d="M3 0h6a1 1 0 0 1 1 1v10a1 1 0 0 1-1 1H3a1 1 0 0 1-1-1V1a1 1 0 0 1 1-1zm0 1.5v7.5h6V1.5z"/></svg>
        202.481.7730
      </li>
      <li>
        <svg viewBox="0 0 12 12"><path d="M0 2.5h12v7H0z M0.8 3.2 6 6.8l5.2-3.6" stroke="#fff" stroke-width="0.9"/></svg>
        lpettibone@galavoyant.com
      </li>
      <li>
        <svg viewBox="0 0 12 12"><circle cx="6" cy="6" r="6"/><path d="M3 3.5c1 .5 1.5 1.5 1 2.5s.5 2 1.5 2.5M7.5 1.5c.5 1 1.5 1.2 2.5 1M8 7c1 0 2 .5 2 1.5" stroke="#fff" stroke-width="0.9" fill="none"/></svg>
        www.galavoyant.com
      </li>
    </ul>

    <div class="divider"></div>
    <address class="address">PO Box 318<br>Washington<br>DC 20019</address>
  </section>

  <section class="card card-back">
    <div class="brand"><span class="brand-dot"></span>galavoyant</div>
  </section>
</body>
</html>
```